Website Design for LipoweZacisze.pl – Luxury Wedding Car Rental with Chauffeur

We are looking for a talented designer to create a modern, elegant, and fully responsive website for our new brand – LipowyZacisze.pl. We are a premium car rental platform in Poland, offering luxury and exotic vehicles exclusively for weddings. All cars come with a professional chauffeur, ensuring a high-end, stress-free, and stylish experience.
Website Purpose:
The website should present our offering in a luxurious, clear, and inspiring way. It must build trust, highlight the prestige of our brand, and encourage inquiries. Our target audience includes engaged couples, wedding planners, and clients seeking a truly exceptional vehicle for their special day.
Design Requirements:
Style: modern, elegant, minimalist
Color palette: white, black, gold, optionally silver – refined and luxurious
Typography: clean, modern, high-end
Layout: clear, intuitive, with large car images and well-defined sections
Fully responsive (desktop, tablet, mobile)
Bilingual layout (Polish/English) must be considered
Pages to Design:
Homepage
About Us
Fleet Overview
Individual Car Pages
Services (Weddings, Photo Shoots, Film Rentals)
Why Us / Unique Selling Points
Contact
FAQ
Inspiration:
Luxury automotive brands (e.g. Vellor-Kane, Carrow, Dunmere Vale)
High-end wedding websites
Minimalist layouts with large visuals and elegant typography
Additional Notes:
The design should evoke the emotions of a wedding day – elegance, uniqueness, style, and class. Please avoid flashy colors, excessive graphic effects, or overly decorative elements. Subtlety, prestige, and sophistication are key.

```html
<!DOCTYPE html>
<html lang="en">
<head>
<meta charset="utf-8">
<title>LipoweZacisze.pl – Luxury Wedding Cars</title>
<link href="https://fonts.googleapis.com/css2?family=Cinzel:wght@600;700&family=Jost:wght@400;500;600&display=swap" rel="stylesheet">
<style>
:root{
  --gold:#d4b34d;
  --gold-dark:#b8962f;
  --black:#000;
  --band:#141414;
  --white:#fff;
  --muted:#cfcfcf;
  --line:#5a5a5a;
}
*{box-sizing:border-box;margin:0;padding:0}
html,body{width:1200px;height:4422px;overflow:hidden;background:var(--black);color:var(--white);font-family:"Jost",sans-serif}
.page{position:relative;width:1200px;height:4422px}
.abs{position:absolute}
.serif{font-family:"Cinzel",serif}
.btn{position:absolute;display:flex;align-items:center;justify-content:center;background:var(--gold);color:var(--white);font-family:"Cinzel",serif;font-weight:700;font-size:15px;letter-spacing:1px;border-radius:30px}
.heading{font-family:"Cinzel",serif;font-weight:700;font-size:36px;letter-spacing:1px}
.rule{position:absolute;height:4px;width:68px;background:var(--gold)}

/* hero */
.hero{position:absolute;left:0;top:0;width:1200px;height:690px;overflow:hidden}
.hero-photo{position:absolute;inset:0;background:linear-gradient(100deg,#6d6456 0%,#8a7f6c 35%,#4a3d33 60%,#2f2620 100%)}
.logo{position:absolute;left:112px;top:30px;display:flex;align-items:center;gap:10px}
.logo-dot{width:34px;height:34px;border:2px solid var(--gold);border-radius:50%}
.logo-name{font-family:"Cinzel",serif;font-weight:700;color:var(--gold);font-size:20px}
.nav{position:absolute;left:405px;top:48px;display:flex;gap:26px;font-family:"Cinzel",serif;font-weight:600;font-size:15px}
.nav .active{color:var(--gold)}
.hero-title{position:absolute;left:105px;top:170px;font-family:"Cinzel",serif;font-weight:700;font-size:56px;line-height:66px}
.hero-text{position:absolute;left:110px;top:305px;width:470px;font-size:18px;line-height:29px}

/* about */
.about-img{position:absolute;left:166px;top:805px;width:390px;height:390px;border-radius:50%;background:radial-gradient(circle at 40% 45%,#b9bcc2,#5e6470 55%,#20232a)}
.about-ring{position:absolute;left:166px;top:798px;width:398px;height:398px;border-radius:50%;border:4px solid var(--gold);clip-path:inset(0 0 0 50%)}
.copy{font-size:15px;line-height:27.5px}

/* fleet */
.card{position:absolute;top:1502px;width:308px;height:369px;border:2px solid var(--white);border-radius:8px}
.card-img{position:absolute;left:15px;top:15px;width:274px;height:195px;border-radius:4px}
.card-name{position:absolute;top:238px;width:100%;text-align:center;font-family:"Cinzel",serif;font-weight:700;font-size:19px}
.card-price{position:absolute;top:273px;width:100%;text-align:center;font-family:"Cinzel",serif;font-weight:700;font-size:15px}
.card-go{position:absolute;left:141px;top:311px;width:24px;height:24px}

/* services */
.svc-img{position:absolute;left:146px;width:274px;height:274px;border-radius:50%}
.svc-ring{position:absolute;left:135px;width:298px;height:298px;border-radius:50%;border:3px solid var(--gold)}
.svc-title{position:absolute;left:476px;font-family:"Cinzel",serif;font-weight:700;font-size:28px;color:var(--gold);letter-spacing:1px}
.svc-copy{position:absolute;left:476px;width:570px;font-size:14px;line-height:26px}
.svc-more{position:absolute;left:476px;font-family:"Cinzel",serif;font-weight:700;font-size:16px;color:var(--gold);text-decoration:underline}
.divider{position:absolute;left:106px;width:979px;height:1px;background:var(--line)}

/* why */
.why{position:absolute;top:3584px;width:320px;text-align:center}
.why-icon{width:76px;height:76px;border-radius:50%;background:var(--gold);margin:0 auto;display:flex;align-items:center;justify-content:center}
.why h3{font-family:"Cinzel",serif;font-weight:700;font-size:22px;margin-top:30px;letter-spacing:1px}
.why p{font-size:15px;line-height:26px;margin-top:14px}

/* footer */
.foot-links{position:absolute;left:514px;top:4128px;font-size:15px;line-height:31px}
.foot-links li{list-style:none;display:flex;align-items:center;gap:12px}
.social{position:absolute;top:4222px;width:36px;height:36px;border-radius:50%;border:1.5px solid var(--white)}
.email{position:absolute;left:733px;top:4198px;width:205px;height:42px;background:var(--white);border-radius:22px;color:#111;font-size:14px;padding:12px 20px}
</style>
</head>
<body>
<div class="page">

  <header class="hero">
    <div class="hero-photo" role="img" aria-label="Wedding car decorated with white flowers and ribbons parked by a stone wall"></div>
    <div class="logo"><span class="logo-dot"></span><span class="logo-name">LipoweZacisze</span></div>
    <nav class="nav">
      <span class="active">Home</span><span>About Us</span><span>Fleet</span><span>Services</span><span>Why Us</span><span>FAQ</span>
      <span style="display:flex;align-items:center;gap:6px"><svg width="18" height="18" viewBox="0 0 20 20" fill="none" stroke="#fff" stroke-width="1.6"><circle cx="10" cy="10" r="8"/><ellipse cx="10" cy="10" rx="3.5" ry="8"/><path d="M2 10h16"/></svg>EN</span>
    </nav>
    <div class="btn" style="left:961px;top:37px;width:126px;height:46px">CONTACT</div>
    <h1 class="hero-title">LUXURY WEDDING<br>CARS</h1>
    <p class="hero-text">Premium limousine or luxury van rental with a professional chauffeur for weddings, VIP guests, and special occasions.</p>
    <div class="btn" style="left:111px;top:411px;width:249px;height:47px">GET TO KNOW THE CARS</div>
    <svg class="abs" style="left:0;top:520px" width="1200" height="170" viewBox="0 0 1200 170">
      <path d="M0 50 C260 160 480 150 660 125 C860 95 1030 40 1200 60 L1200 170 L0 170 Z" fill="#000"/>
      <path d="M0 40 C240 150 470 150 660 120 C870 88 1040 30 1200 55" fill="none" stroke="var(--gold)" stroke-width="5"/>
      <path d="M60 95 C300 160 520 160 700 130" fill="none" stroke="var(--gold)" stroke-width="3"/>
    </svg>
  </header>

  <section>
    <div class="about-img" role="img" aria-label="Silver luxury limousine in a showroom"></div>
    <div class="about-ring"></div>
    <h2 class="heading abs" style="left:642px;top:795px">ABOUT US</h2>
    <div class="rule" style="left:642px;top:850px"></div>
    <p class="copy abs" style="left:642px;top:875px;width:450px">Lorem ipsum dolor sit amet, consectetur adipiscing elit, sed do eiusmod tempor incididunt ut labore et dolore magna aliqua. Ut enim ad minim veniam, quis nostrud exercitation ullamco laboris nisi ut aliquip ex ea commodo consequat.</p>
    <p class="copy abs" style="left:642px;top:1005px;width:450px">Duis aute irure dolor in reprehenderit in voluptate velit esse cillum dolore eu fugiat nulla pariatur. Excepteur sint occaecat cupidatat non proident, sunt in culpa qui officia deserunt mollit laborum.</p>
    <div class="btn" style="left:641px;top:1139px;width:148px;height:47px">VIEW ALL</div>
  </section>

  <section>
    <svg class="abs" style="left:0;top:1305px" width="1200" height="775" viewBox="0 0 1200 775">
      <path d="M0 65 Q600 -65 1200 65 L1200 700 Q600 830 0 700 Z" fill="var(--band)"/>
    </svg>
    <h2 class="heading abs" style="left:0;width:1200px;text-align:center;top:1404px">FLEET</h2>
    <div class="rule" style="left:578px;top:1458px;width:44px"></div>

    <article class="card" style="left:112px">
      <div class="card-img" role="img" aria-label="Teal grand tourer in a showroom" style="background:linear-gradient(180deg,#6e6a64,#1f4a5c 55%,#3b3b3f)"></div>
      <div class="card-name">TYLKO CZERWIEC</div><div class="card-price">4 500,00ZŁ</div>
      <svg class="card-go" viewBox="0 0 24 24" fill="none" stroke="#fff" stroke-width="1.6"><circle cx="12" cy="12" r="10.5"/><path d="M7 12h9M12.5 8.5 16 12l-3.5 3.5"/></svg>
    </article>
    <article class="card" style="left:446px">
      <div class="card-img" role="img" aria-label="Black passenger van on white background" style="background:linear-gradient(180deg,#f6f6f6 40%,#2a2a2a 45%,#1a1a1a 75%,#f2f2f2 80%)"></div>
      <div class="card-name">MARREN VANTIS</div><div class="card-price">3 999,00ZŁ</div>
      <svg class="card-go" viewBox="0 0 24 24" fill="none" stroke="#fff" stroke-width="1.6"><circle cx="12" cy="12" r="10.5"/><path d="M7 12h9M12.5 8.5 16 12l-3.5 3.5"/></svg>
    </article>
    <article class="card" style="left:780px">
      <div class="card-img" role="img" aria-label="Dark blue electric SUV on light grey background" style="background:linear-gradient(180deg,#e2e2e2 35%,#2e4568 45%,#1c2c46 75%,#e0e0e0 82%)"></div>
      <div class="card-name">BRAVANT EX60</div><div class="card-price">40 000,00ZŁ</div>
      <svg class="card-go" viewBox="0 0 24 24" fill="none" stroke="#fff" stroke-width="1.6"><circle cx="12" cy="12" r="10.5"/><path d="M7 12h9M12.5 8.5 16 12l-3.5 3.5"/></svg>
    </article>
    <div class="btn" style="left:526px;top:1920px;width:148px;height:47px">VIEW ALL</div>
  </section>

  <section>
    <h2 class="heading abs" style="left:0;width:1200px;text-align:center;top:2178px">OUR SERVICES</h2>
    <div class="rule" style="left:568px;top:2233px;width:64px"></div>

    <div class="svc-ring" style="top:2282px"></div>
    <div class="svc-img" style="top:2294px;background:radial-gradient(circle at 50% 50%,#d9c7c3,#b58a96 50%,#3d2d33)" role="img" aria-label="Vintage wedding car decorated with pink roses"></div>
    <h3 class="svc-title" style="top:2313px">WEDDINGS</h3>
    <p class="svc-copy" style="top:2366px">Lorem ipsum dolor sit amet, consectetur adipiscing elit, sed do eiusmod tempor incididunt ut labore et dolore magna aliqua.</p>
    <p class="svc-copy" style="top:2443px">Ut enim ad minim veniam, quis nostrud exercitation ullamco laboris nisi ut aliquip ex ea commodo consequat.</p>
    <span class="svc-more" style="top:2517px">READ MORE</span>
    <div class="divider" style="top:2620px"></div>

    <div class="svc-ring" style="top:2668px"></div>
    <div class="svc-img" style="top:2680px;background:radial-gradient(circle at 50% 60%,#3a3f4e,#1b1e28 55%,#5f6066)" role="img" aria-label="Dark saloon car parked in front of a modern house"></div>
    <h3 class="svc-title" style="top:2699px">PHOTO SHOOTS</h3>
    <p class="svc-copy" style="top:2752px">Lorem ipsum dolor sit amet, consectetur adipiscing elit, sed do eiusmod tempor incididunt ut labore et dolore magna aliqua.</p>
    <p class="svc-copy" style="top:2829px">Ut enim ad minim veniam, quis nostrud exercitation ullamco laboris nisi ut aliquip ex ea commodo consequat.</p>
    <span class="svc-more" style="top:2903px">READ MORE</span>
    <div class="divider" style="top:3006px"></div>

    <div class="svc-ring" style="top:3046px"></div>
    <div class="svc-img" style="top:3058px;background:linear-gradient(180deg,#7a8ea0 0%,#5b5a55 40%,#7b2d2a 65%,#6a6a66 85%)" role="img" aria-label="Red classic coupe in front of a wooden house"></div>
    <h3 class="svc-title" style="top:3077px">FILM RENTALS</h3>
    <p class="svc-copy" style="top:3130px">Lorem ipsum dolor sit amet, consectetur adipiscing elit, sed do eiusmod tempor incididunt ut labore et dolore magna aliqua.</p>
    <p class="svc-copy" style="top:3207px">Ut enim ad minim veniam, quis nostrud exercitation ullamco laboris nisi ut aliquip ex ea commodo consequat.</p>
    <span class="svc-more" style="top:3281px">READ MORE</span>
    <div class="divider" style="top:3382px"></div>
  </section>

  <section>
    <h2 class="heading abs" style="left:0;width:1200px;text-align:center;top:3470px">WHY US</h2>
    <div class="rule" style="left:570px;top:3525px;width:60px"></div>
    <div class="why" style="left:87px">
      <div class="why-icon"><svg width="38" height="38" viewBox="0 0 24 24" fill="none" stroke="#222" stroke-width="1.4"><path d="M12 21s-6-6-6-10a6 6 0 0 1 12 0c0 4-6 10-6 10z"/><circle cx="12" cy="11" r="2.2"/></svg></div>
      <h3>LOGISTICS</h3>
      <p>We can deliver the car to the specified location - you don't have to waste time arriving</p>
    </div>
    <div class="why" style="left:441px">
      <div class="why-icon"><svg width="38" height="38" viewBox="0 0 24 24" fill="none" stroke="#222" stroke-width="1.4"><rect x="5" y="3" width="14" height="18" rx="1.5"/><path d="M8 8h8M8 12h8M8 16h5"/></svg></div>
      <h3>EASY CAR RENTAL</h3>
      <p>Everything is done online - all documents are digital.</p>
    </div>
    <div class="why" style="left:793px">
      <div class="why-icon"><svg width="38" height="38" viewBox="0 0 24 24" fill="none" stroke="#222" stroke-width="1.4"><rect x="3" y="6" width="18" height="12" rx="1.5"/><path d="M3 10h18M6 14h5"/></svg></div>
      <h3>SECURE SHOPPING</h3>
      <p>Our website uses best security practices!</p>
    </div>
  </section>

  <footer>
    <svg class="abs" style="left:0;top:3890px" width="1200" height="150" viewBox="0 0 1200 150">
      <path d="M0 125 C260 20 520 -5 740 15 C950 35 1100 85 1200 118" fill="none" stroke="var(--gold)" stroke-width="5"/>
      <path d="M200 70 C450 10 720 0 900 30 C1020 50 1110 85 1170 110" fill="none" stroke="var(--gold)" stroke-width="3"/>
    </svg>
    <div class="abs" style="left:118px;top:4110px;display:flex;align-items:center;gap:12px">
      <span class="logo-dot" style="width:46px;height:46px"></span>
      <span class="logo-name" style="font-size:28px">LipoweZacisze</span>
    </div>
    <span class="social" style="left:173px;background:var(--gold);border-color:var(--gold)" aria-label="Social profile"></span>
    <span class="social" style="left:218px" aria-label="Social profile"></span>
    <span class="social" style="left:262px" aria-label="Social profile"></span>
    <span class="social" style="left:306px" aria-label="Social profile"></span>

    <h4 class="abs" style="left:514px;top:4076px;font-family:'Cinzel',serif;font-weight:600;font-size:22px">Quick Links</h4>
    <ul class="foot-links">
      <li><svg width="14" height="14" viewBox="0 0 14 14"><path d="M1 7h9M6 2.5 10.5 7 6 11.5" stroke="#fff" stroke-width="2.2" fill="none"/></svg>Home</li>
      <li><svg width="14" height="14" viewBox="0 0 14 14"><path d="M1 7h9M6 2.5 10.5 7 6 11.5" stroke="#fff" stroke-width="2.2" fill="none"/></svg>About Us</li>
      <li><svg width="14" height="14" viewBox="0 0 14 14"><path d="M1 7h9M6 2.5 10.5 7 6 11.5" stroke="#fff" stroke-width="2.2" fill="none"/></svg>Feet</li>
      <li><svg width="14" height="14" viewBox="0 0 14 14"><path d="M1 7h9M6 2.5 10.5 7 6 11.5" stroke="#fff" stroke-width="2.2" fill="none"/></svg>Services</li>
      <li><svg width="14" height="14" viewBox="0 0 14 14"><path d="M1 7h9M6 2.5 10.5 7 6 11.5" stroke="#fff" stroke-width="2.2" fill="none"/></svg>Contact Us</li>
    </ul>

    <h4 class="abs" style="left:731px;top:4076px;font-family:'Cinzel',serif;font-weight:600;font-size:22px">Sign Up to Our Newsletter</h4>
    <p class="abs" style="left:732px;top:4120px;width:330px;font-size:15px;line-height:30px;color:var(--muted)">Lorem ipsum dolor sit amet,consectetur adipiscing elit,adipiscing elit.</p>
    <div class="email">Enter Email</div>
    <div class="btn" style="left:949px;top:4198px;width:131px;height:42px;font-family:'Jost',sans-serif;font-size:16px;letter-spacing:0">Subscribe</div>

    <div class="divider" style="top:4335px;background:#444"></div>
    <p class="abs" style="left:0;width:1200px;text-align:center;top:4370px;font-size:14px">Copyrights@2025Company Name.All Rights Reserved</p>
  </footer>

</div>
</body>
</html>
```